Tralven Networks co-marketing flier

We want a flier that our partners (IT consultants) can hand out to their clients and that we can send to local businesses on their behalf to demonstrate that they can help customers purchase a phone system that has professional features that they would expect in a phone solution that costs thousands of dollars.

We want the brochure to look very professional with excellent layout and use of space.

The Tralven Networks corporate colour is green and more details can be found at www.tralvennetworks-example.com.au.

We have attached a draft Word document that contains most of the information we need but please present the information in the way YOU believe it should be laid out.

We are looking for a designer who understands the concept and uses their own skills to produce a work of art.

Target Market(s)

small businesses that want to save money but also want a modern phone with lots of features

Industry/Entity Type

Marketing

Requirements
Must have
• Must have an image of the main phone and a cordless handset to indicate that they don't need wires to set the system up.

Must have our logo and website address

Must have a box or some "placeholder" where our partners can stamp or insert their details.

Must have a "call to action" saying "Contact us for a quote"

```html
<!DOCTYPE html>
<html lang="en">
<head>
<meta charset="utf-8">
<title>Tralven Networks – New Phone System Flier</title>
<link rel="stylesheet" href="https://fonts.googleapis.com/css2?family=Anton&family=Archivo+Black&family=Arimo:wght@400;700&display=swap">
<style>
  :root {
    --forest: #123421;
    --brand-green: #1a7a34;
    --heading-green: #0e5a26;
    --cream: #f8efad;
    --stamp-fill: #c8e3d2;
    --stamp-edge: #fdf6c2;
    --ink: #1d1d1d;
    --pale-green: #bfe0c9;
    --paper: #ffffff;
    --backdrop: #f2f2f2;
    --photo-dark: #3a3d40;
    --photo-light: #c9ccce;
  }
  * { box-sizing: border-box; margin: 0; padding: 0; }
  html, body { width: 1200px; height: 1200px; overflow: hidden; background: var(--backdrop); }
  body { position: relative; font-family: "Arimo", Arial, sans-serif; color: var(--ink); }

  .flier {
    position: absolute; left: 151px; top: 32px;
    width: 869px; height: 1125px;
    background: var(--paper);
    overflow: hidden;
  }
  .feature-column {
    position: absolute; left: 0; top: 0;
    width: 332px; height: 100%;
    background: var(--forest);
  }

  .headline { position: absolute; top: 51px; height: 61px; display: flex; align-items: center; justify-content: center; white-space: nowrap; }
  .headline--looking {
    left: 27px; width: 305px; background: var(--paper);
    font-family: "Anton", sans-serif; font-size: 52px; letter-spacing: 8px;
    color: var(--forest); padding-left: 8px;
  }
  .headline--phone {
    left: 332px; width: 497px; background: var(--forest);
    font-family: "Anton", sans-serif; font-size: 50px; letter-spacing: 0.5px;
    color: var(--paper);
  }
  .headline--system {
    position: absolute; left: 387px; top: 148px; white-space: nowrap;
    font-family: "Archivo Black", sans-serif; font-size: 31px; line-height: 34px;
    letter-spacing: 31px; color: var(--forest);
  }
  .intro {
    position: absolute; left: 379px; top: 200px; width: 385px;
    font-weight: 700; font-size: 17px; line-height: 21px;
  }

  .features-title {
    position: absolute; left: 0; width: 332px; top: 250px; text-align: center;
    font-family: "Anton", sans-serif; font-weight: 400; font-size: 26px; line-height: 30px;
    color: var(--cream); letter-spacing: 0.5px;
  }
  .features-subtitle {
    position: absolute; left: 0; width: 332px; top: 280px; text-align: center;
    font-weight: 700; font-size: 17px; line-height: 20px; color: var(--paper);
  }
  .feature-list {
    position: absolute; left: 43px; top: 339px; width: 250px;
    list-style: none; color: var(--paper);
    font-weight: 700; font-size: 19px; line-height: 25px;
  }
  .feature-list li { position: relative; padding-left: 18px; margin-bottom: 27px; }
  .feature-list li::before { content: "•"; position: absolute; left: 0; font-size: 15px; }
  .feature-list .feature-note { display: block; font-size: 12px; line-height: 22px; white-space: nowrap; }

  .stamp-area {
    position: absolute; left: 23px; top: 888px; width: 293px; height: 200px;
    background: var(--stamp-fill); border: 5px solid var(--stamp-edge);
    border-radius: 80px;
  }

  .product-photo { position: absolute; border-radius: 24px; }
  .product-photo--desk {
    left: 310px; top: 272px; width: 507px; height: 303px;
    background: linear-gradient(160deg, var(--photo-light), var(--photo-dark));
  }
  .product-photo--cordless {
    left: 645px; top: 551px; width: 193px; height: 407px; border-radius: 60px;
    background: linear-gradient(180deg, var(--photo-dark), #151617);
  }

  .cta-lead {
    position: absolute; left: 392px; top: 718px;
    font-family: "Archivo Black", sans-serif; font-size: 28px; line-height: 38px;
    color: var(--heading-green);
  }
  .cta-action {
    position: absolute; left: 393px; top: 801px;
    font-weight: 700; font-size: 18px;
  }

  .brand-name {
    position: absolute; left: 393px; top: 966px;
    display: flex; align-items: center; gap: 10px;
    font-family: "Arimo", sans-serif; font-weight: 700; font-size: 30px;
    color: var(--brand-green); white-space: nowrap;
  }
  .brand-name .brand-dot { width: 14px; height: 14px; border-radius: 50%; background: var(--brand-green); }
  .company-details {
    position: absolute; left: 393px; top: 1024px;
    font-weight: 700; font-size: 16px; line-height: 20px; white-space: nowrap;
  }
  .company-details .abn { color: var(--pale-green); }
</style>
</head>
<body>
  <main class="flier">
    <div class="feature-column"></div>

    <h1>
      <span class="headline headline--looking">LOOKING</span>
      <span class="headline headline--phone">FOR A NEW PHONE</span>
      <span class="headline--system">SYSTEM?</span>
    </h1>

    <p class="intro">Our proven VoIP solution comes with all the professional features to service an office of up to 6 people.</p>

    <h2 class="features-title">FEATURES INCLUDE</h2>
    <p class="features-subtitle">But Not Limited To</p>
    <ul class="feature-list">
      <li>very low rental rates*</li>
      <li>10c local and national<br>calls unlimited</li>
      <li>voicemail-to-email</li>
      <li>Bluetooth-to-mobile</li>
      <li>direct-to-dial to every<br>extension</li>
      <li>number portability<span class="feature-note">(keep your number when you move)</span></li>
      <li>call records via<br>spreadsheet</li>
      <li>flat rate local and<br>national calls</li>
    </ul>

    <div class="stamp-area" aria-label="Space for partner details"></div>

    <div class="product-photo product-photo--desk" role="img" aria-label="Photo of a silver and black desk phone base with corded handset and colour screen"></div>
    <div class="product-photo product-photo--cordless" role="img" aria-label="Photo of a black cordless handset standing in its charging cradle"></div>

    <p class="cta-lead">It’s Cheaper<br>Than You Think</p>
    <p class="cta-action">Contact Us For A Quote</p>

    <div class="brand-name"><span class="brand-dot"></span>Tralven Networks</div>
    <p class="company-details">
      Kestrelline (456 Holdings Pty Ltd)<br>
      <span class="abn">ABN: 12 345 678 901</span><br>
      www.tralvennetworks-example.com.au
    </p>
  </main>
</body>
</html>
```